BQL Groundworks & Freight Business Card

Can you please design a business card for an Earthworks, Haulage truck and machinery hire company. They also provide sand soil and mulch supply, as well as screening of products. Can you re-create the logo from the attached but add BQL Groundworks & Freight just use the three diamond design.

Target Market(s)

Earthmoving and Transport, Landscapers, Construction

Contact Information for Business Card

ABN 52 907 334 816, Doug Pelham, Managing Director, BQL Groundworks & Freight Mobile 0438 256 904 Email bqlfreight2010@mailvane.net

Font styles to use
Sans Serif

Colors
ec1f27
000000
cbcbcb
ffffff

Requirements
Must have
• Listed on the back, Earthworks | Haulage | Truck and Machinery Hire | Sand, Soil & Mulch Supply | Screening of Products
Nice to have
• Would be good for it to look appealing to a mans man, because it relates to heavy machinery, earthworks, construction etc. Black, red and white would be good maybe with a bit of silver somewhere.
Should not have
• not sure

```html
<!DOCTYPE html>
<html lang="en">
<head>
<meta charset="utf-8">
<title>BQL Groundworks &amp; Freight – Business Card</title>
<link rel="stylesheet" href="https://fonts.googleapis.com/css2?family=Bebas+Neue&family=Montserrat:wght@600;700&display=swap">
<style>
  :root {
    --red: #ec1f27;
    --red-deep: #9c151b;
    --black: #000000;
    --charcoal: #2a2a2a;
    --silver: #cbcbcb;
    --white: #ffffff;
    --grey-text: #6b6b6b;
    --page: #ffffff;
  }
  * { margin: 0; padding: 0; box-sizing: border-box; }
  html, body {
    width: 1200px; height: 1200px; overflow: hidden;
    background: var(--page);
  }
  .canvas { position: relative; width: 1200px; height: 1200px; }

  .card {
    position: absolute; left: 244px; width: 733px; height: 476px; overflow: hidden;
  }

  /* Front */
  .card-front {
    top: 82px;
    background: radial-gradient(ellipse at 50% 45%, var(--charcoal) 0%, #111 55%, var(--black) 100%);
  }
  .card-front .swoosh { position: absolute; inset: 0; width: 100%; height: 100%; }
  .brand {
    position: absolute; left: 0; right: 0; top: 100px;
    text-align: center; color: var(--white);
    font-family: "Montserrat", sans-serif; font-weight: 700;
  }
  .brand-mark {
    display: inline-flex; align-items: center; gap: 22px;
    font-size: 118px; line-height: 1; letter-spacing: 14px;
  }
  .brand-square {
    width: 46px; height: 46px; background: var(--red);
  }
  .brand-name {
    margin-top: 34px; font-size: 30px; letter-spacing: 2px; line-height: 1.2;
  }

  /* Back */
  .card-back { top: 614px; background: var(--white); }
  .person {
    position: absolute; left: 72px; top: 60px;
    font-family: "Bebas Neue", sans-serif; font-size: 56px; line-height: 1;
    color: var(--black);
  }
  .role {
    position: absolute; left: 72px; top: 118px;
    font-family: "Montserrat", sans-serif; font-weight: 700; font-size: 16.5px;
    letter-spacing: 0.6px; color: var(--grey-text); white-space: nowrap;
  }
  .role .sep { color: var(--red-deep); font-size: 11px; margin: 0 6px; vertical-align: 2px; }

  .contact { position: absolute; left: 76px; top: 190px; list-style: none; }
  .contact li {
    display: flex; align-items: center; height: 34px;
    font-family: "Montserrat", sans-serif; font-weight: 700; font-size: 22px;
    color: var(--grey-text);
  }
  .contact svg { width: 28px; height: 26px; margin-right: 12px; flex: none; }

  .abn {
    position: absolute; left: 72px; top: 292px;
    font-family: "Montserrat", sans-serif; font-weight: 700; font-size: 22px;
    color: var(--grey-text);
  }

  .services-band {
    position: absolute; left: 0; bottom: 0; width: 100%; height: 103px;
    background: linear-gradient(90deg, var(--red-deep) 0%, #b81c22 100%);
  }
  .band-mark {
    position: absolute; left: 48px; top: 32px;
    display: flex; align-items: center; gap: 10px;
    font-family: "Montserrat", sans-serif; font-weight: 700; font-size: 34px;
    letter-spacing: 5px; color: var(--white); line-height: 1;
  }
  .band-mark .brand-square { width: 16px; height: 16px; background: var(--white); }
  .services {
    position: absolute; left: 258px; top: 24px;
    font-family: "Bebas Neue", sans-serif; font-size: 25px; line-height: 30px;
    color: var(--white); white-space: nowrap;
  }
  .services .bar { margin: 0 6px; }
</style>
</head>
<body>
<main class="canvas">

  <section class="card card-front" aria-label="Business card front">
    <svg class="swoosh" viewBox="0 0 733 476" preserveAspectRatio="none" aria-hidden="true">
      <defs>
        <linearGradient id="silverBand" x1="0" x2="1" y1="0" y2="0">
          <stop offset="0" stop-color="#7a7a7a"/>
          <stop offset="0.3" stop-color="#f2f2f2"/>
          <stop offset="0.5" stop-color="#9a9a9a"/>
          <stop offset="0.65" stop-color="#2e2e2e"/>
          <stop offset="0.85" stop-color="#cbcbcb"/>
          <stop offset="1" stop-color="#8a8a8a"/>
        </linearGradient>
        <linearGradient id="redBase" x1="0" x2="1" y1="0" y2="0">
          <stop offset="0" stop-color="#8e1217"/>
          <stop offset="1" stop-color="#b81c22"/>
        </linearGradient>
      </defs>
      <path d="M0,322 Q330,470 733,318 L733,346 Q340,480 0,352 Z" fill="url(#silverBand)"/>
      <path d="M0,352 Q340,480 733,346 L733,476 L0,476 Z" fill="url(#redBase)"/>
    </svg>
    <div class="brand">
      <div class="brand-mark"><span class="brand-square"></span>BQL</div>
      <div class="brand-name">GROUNDWORKS<br>&amp; FREIGHT</div>
    </div>
  </section>

  <section class="card card-back" aria-label="Business card back">
    <h1 class="person">DOUG PELHAM</h1>
    <p class="role">MANAGING DIRECTOR<span class="sep">◆</span>BQL GROUNDWORKS &amp; FREIGHT</p>

    <ul class="contact">
      <li>
        <svg viewBox="0 0 24 24" aria-hidden="true"><path fill="#9c151b" d="M6.6 2.5l3 3.6-1.9 2.4c1.2 2.7 3.2 4.8 5.9 6.1l2.4-1.9 3.6 3-2 3.6C10.8 19.1 4.9 13.2 3 6.4z"/></svg>
        0438 256 904
      </li>
      <li>
        <svg viewBox="0 0 24 24" aria-hidden="true"><rect x="2" y="5" width="20" height="14" fill="none" stroke="#9c151b" stroke-width="2"/><path d="M2 5l10 8 10-8M2 19l8-7M22 19l-8-7" fill="none" stroke="#9c151b" stroke-width="2"/></svg>
        bqlfreight2010@mailvane.net
      </li>
    </ul>

    <p class="abn">ABN 52 907 334 816</p>

    <div class="services-band">
      <div class="band-mark"><span class="brand-square"></span>BQL</div>
      <p class="services">
        EARTHWORKS<span class="bar">|</span>HAULAGE<span class="bar">|</span>TRUCK AND MACHINERY HIRE<br>
        SAND, SOIL &amp; MULCH SUPPLY<span class="bar">|</span>SCREENING OF PRODUCTS
      </p>
    </div>
  </section>

</main>
</body>
</html>
```